West Australian based aspiring best selling novelist needs a book cover design

I have a completed manuscript for a fiction novel about 3 women whose partners work away in fly in fly out (FIFO) jobs. One woman has three young kids (boy, 8, boy 6 and girl 18months old), one woman is the first woman's sister and is young and beautiful but a bit troubled and one woman works on reception at a strip club. All three want to be independent but still miss their lovers. Location is the Midwest of Western Australia where there are beautiful beaches, blue skies and crayfish. The title is 'Seven Kites Over the Salt Flats.' Author's name is Ruth Dalby. I need a book cover design. I am unsure whether to try and capture the spirit of those women or the landscape or do a simple graphic design like crosses on a dateless calendar, counting down the days (Two weeks crossed off then one happy week when the lover is home and then another two sad weeks). The final design should lure people in to want to read the text. Thank you

Target Market(s)
Women, particularly those who are struggling with being a stay at home lover.

Must Have:
- Soul, an understanding of the complexity of loneliness. The women are strong and interesting- not flaky. This is NOT a romance novel. It is a quirky story with heart.

Nice to Have:
- A design that is striking but not too busy

Should Not Have:
- No trashy images of women. Should NOT look like a romance novel.

Target Market(s)

Women 18 upwards

Industry/Entity Type

Book Publisher

Font styles to use
Other font styles liked:
• unsure

Requirements
Must have
• A bit of quirkiness, soul, loneliness, independence
Nice to have
• Something striking but not too busy. I trust your skills!
Should not have
• Not look like a romance novel. The genre is more contemporary chick literature

```html
<!DOCTYPE html>
<html lang="en">
<head>
<meta charset="utf-8">
<title>Seven Kites Over the Salt Flats — Ruth Dalby</title>
<link rel="stylesheet" href="https://fonts.googleapis.com/css2?family=Bebas+Neue&family=Tinos&display=swap">
<style>
  :root {
    --page: #ffffff;
    --cover: #ffffff;
    --cover-edge: #d6d6d6;
    --title-red: #f2313d;
    --author-ink: #111111;
    --sky-top: #a9cbe8;
    --sky-mid: #c9dced;
    --sky-low: #e4ebf0;
  }
  * { margin: 0; padding: 0; box-sizing: border-box; }
  html, body {
    width: 1200px;
    height: 1200px;
    overflow: hidden;
    background: var(--page);
  }
  .stage {
    position: relative;
    width: 1200px;
    height: 1200px;
  }
  .cover {
    position: absolute;
    left: 230px;
    top: 45px;
    width: 740px;
    height: 1110px;
    background: var(--cover);
    border: 1px solid var(--cover-edge);
    overflow: hidden;
  }
  .cover__art {
    position: absolute;
    left: 0;
    top: 0;
    width: 740px;
    height: 540px;
  }
  .cover__title {
    position: absolute;
    left: 0;
    width: 100%;
    text-align: center;
    font-family: "Bebas Neue", "Oswald", sans-serif;
    color: var(--title-red);
    line-height: 1;
    letter-spacing: -0.01em;
    white-space: nowrap;
  }
  .cover__title--small { font-size: 94px; }
  .cover__title--large { font-size: 178px; }
  .cover__title--largest { font-size: 188px; }
  .line-1 { top: 548px; }
  .line-2 { top: 622px; }
  .line-3 { top: 690px; }
  .line-4 { top: 825px; }
  .cover__author {
    position: absolute;
    left: 0;
    width: 100%;
    top: 1000px;
    text-align: center;
    font-family: "Tinos", "Times New Roman", serif;
    font-size: 72px;
    color: var(--author-ink);
    line-height: 1;
  }
</style>
</head>
<body>
  <main class="stage">
    <article class="cover">
      <svg class="cover__art" viewBox="0 0 740 540" role="img" aria-label="Illustration of a woman's tearful face framed by her hands against a pale blue sky">
        <defs>
          <linearGradient id="sky" x1="0" y1="0" x2="0" y2="1">
            <stop offset="0" stop-color="var(--sky-top)"/>
            <stop offset="0.5" stop-color="var(--sky-mid)"/>
            <stop offset="1" stop-color="var(--sky-low)"/>
          </linearGradient>
        </defs>
        <polygon fill="url(#sky)" points="45,0 700,0 695,90 625,180 565,330 475,420 398,532 362,420 250,300 140,262 60,80"/>
      </svg>

      <h1 class="cover__heading">
        <span class="cover__title cover__title--small line-1">Seven Kites</span>
        <span class="cover__title cover__title--small line-2">Over The</span>
        <span class="cover__title cover__title--large line-3">Salt</span>
        <span class="cover__title cover__title--largest line-4">Flats</span>
      </h1>

      <p class="cover__author">Ruth Dalby</p>
    </article>
  </main>
</body>
</html>
```